E learning Platform for privacy

Current website is as below and its more of a shell.
I need someone to take the text and content and design it properly.
https://study.norvalhub.example/

After that, design has to be implemented with quillbrick and wordpress
https://quillbrick.example/

```html
<!DOCTYPE html>
<html lang="en">
<head>
<meta charset="utf-8">
<title>Courses – Norval Learning Centre</title>
<link href="https://fonts.googleapis.com/css2?family=Poppins:wght@400;500;600;700&display=swap" rel="stylesheet">
<style>
:root{
  --orange:#e65c24;
  --amber:#f39322;
  --ink:#111111;
  --text:#444444;
  --muted:#6b6b6b;
  --page:#f7f7f7;
  --card:#ffffff;
  --footer:#474747;
  --soft:#fdebdc;
  --blob:#ececec;
}
*{margin:0;padding:0;box-sizing:border-box}
html,body{width:1200px;height:2204px;overflow:hidden}
body{position:relative;background:var(--page);font-family:'Poppins',sans-serif;color:var(--ink)}
.abs{position:absolute}
.backdrop{position:absolute;left:0;top:0}
.brand{left:89px;top:24px}
.brand-name{font-size:32px;font-weight:600;color:var(--orange);letter-spacing:4px;line-height:1}
.brand-tag{font-size:7px;letter-spacing:4.5px;color:var(--text);margin-top:4px}
.nav{left:476px;top:36px;display:flex;gap:28px;font-size:15px;font-weight:500}
.nav a{color:var(--ink);text-decoration:none}
.nav a.active{color:var(--orange)}
.signin{left:934px;top:36px;font-size:15px;font-weight:500}
.signup{left:1008px;top:31px;width:103px;height:33px;border-radius:17px;background:var(--amber);color:#fff;font-size:15px;font-weight:500;display:flex;align-items:center;justify-content:center}
.crumbs{left:87px;top:178px;font-size:18px;color:var(--text)}
.crumbs span{margin:0 10px}
.page-title{left:87px;top:194px;font-size:53px;font-weight:700;line-height:1.15}
.hero-art{left:640px;top:138px;width:469px;height:195px;border-radius:8px;background:linear-gradient(120deg,#f6c531 0%,#e94e5f 35%,#1e8fe5 60%,#7cc21f 100%)}
.search-box{left:89px;top:424px;width:284px;height:109px;border-radius:14px;background:var(--orange);padding:20px 27px}
.search-box h3{color:#fff;font-size:21px;font-weight:600;line-height:1}
.search-input{margin-top:8px;margin-left:-4px;width:236px;height:34px;border-radius:17px;background:#fff;font-size:12px;font-weight:500;color:var(--muted);padding:9px 16px}
.categories{left:89px;top:548px;width:283px;height:463px;border-radius:14px;background:var(--card);box-shadow:0 4px 20px rgba(0,0,0,.04)}
.cat-head{left:24px;top:38px;font-size:23px;font-weight:600}
.cat-main{left:27px;font-size:18px;font-weight:600;color:var(--orange);width:228px;display:flex;justify-content:space-between;align-items:center;white-space:nowrap}
.cat-sub{left:40px;top:156px;font-size:15.5px;color:var(--text);line-height:26.8px}
.section-title{left:419px;top:410px;font-size:32px;font-weight:600}
.card{width:338px;height:344px;border-radius:16px;background:var(--card);box-shadow:0 4px 20px rgba(0,0,0,.05)}
.thumb{position:absolute;left:11px;top:15px;width:315px;height:172px;border-radius:10px}
.card h4{position:absolute;left:24px;top:201px;font-size:18px;font-weight:600;white-space:nowrap}
.card p{position:absolute;left:24px;top:234px;width:282px;font-size:13.5px;color:var(--muted);line-height:18px}
.meta{position:absolute;left:24px;top:279px;font-size:14px;font-weight:600;color:var(--text);line-height:21px}
.meta div{display:flex;align-items:center;gap:7px}
.meta svg{flex:none}
.start{position:absolute;left:216px;top:284px;width:111px;height:34px;border-radius:17px;background:var(--soft);color:var(--amber);font-size:13px;font-weight:600;display:flex;align-items:center;justify-content:center}
.news-title{left:0;top:1745px;width:1200px;text-align:center;color:#fff;font-size:36px;font-weight:700;line-height:38px}
.news-form{left:240px;top:1849px;width:720px;height:51px;border-radius:26px;background:#fff;border:2px solid #fff}
.news-form .ph{position:absolute;left:22px;top:14px;font-size:15px;color:var(--muted)}
.news-form .btn{position:absolute;right:0;top:0;width:180px;height:47px;border-radius:24px;background:var(--orange);color:#fff;font-size:17px;font-weight:700;display:flex;align-items:center;justify-content:center}
.foot-brand{left:150px;top:1966px;width:270px;text-align:center;color:#fff}
.foot-brand .brand-name{color:#fff;font-size:38px;letter-spacing:5px}
.foot-brand .brand-tag{color:#fff;font-size:8px;letter-spacing:6px;margin-top:6px}
.foot-brand p{font-size:14px;line-height:24px;margin-top:10px}
.foot-col{top:1966px;color:#fff}
.foot-col h5{font-size:20px;font-weight:600;margin-bottom:7px}
.foot-col a{display:block;font-size:14.5px;color:#e4e4e4;text-decoration:none;line-height:25.8px}
.foot-rule{left:89px;top:2151px;width:1022px;height:1px;background:#5e5e5e}
.copyright{left:89px;top:2169px;font-size:14.5px;color:#fff}
.socials{left:1019px;top:2174px;display:flex;gap:12px}
.socials span{width:11px;height:11px;border-radius:50%;background:#fff}
.to-top{left:1134px;top:2134px;width:34px;height:34px;border-radius:50%;background:var(--amber);display:flex;align-items:center;justify-content:center}
</style>
</head>
<body>

<svg class="backdrop" width="1200" height="2204" viewBox="0 0 1200 2204" aria-hidden="true">
  <path d="M1160,0 C1120,80 1180,200 1110,270 C1040,340 900,400 820,330 C780,280 830,220 900,190 C980,160 1060,80 1080,0 Z" fill="var(--blob)"/>
  <path d="M0,1773 C300,1765 470,1650 600,1545 C680,1485 790,1468 900,1478 C1040,1492 1140,1555 1200,1605 L1200,2204 L0,2204 Z" fill="var(--footer)"/>
  <path d="M560,1578 C640,1500 760,1470 900,1478 C1040,1492 1140,1555 1200,1605" fill="none" stroke="var(--amber)" stroke-width="14"/>
</svg>

<div class="abs brand">
  <div class="brand-name">NORVAL</div>
  <div class="brand-tag">LEARNING CENTRE</div>
</div>
<nav class="abs nav">
  <a href="#">Home</a><a href="#">About Us</a><a href="#">Blogs</a><a href="#" class="active">Courses</a><a href="#">Contact Us</a>
</nav>
<div class="abs signin">Sign In</div>
<div class="abs signup">Sign Up</div>

<div class="abs crumbs">Home<span>›</span>Courses</div>
<h1 class="abs page-title">Courses</h1>
<div class="abs hero-art" role="img" aria-label="Illustration of an online learner with a laptop, graduation cap, certificate and video player"></div>

<aside>
  <div class="abs search-box">
    <h3>SEARCH</h3>
    <div class="search-input">Seareh Course</div>
  </div>
  <div class="abs categories">
    <div class="abs cat-head">CATEGORIES</div>
    <div class="abs cat-main" style="top:82px">All Courses</div>
    <div class="abs cat-main" style="top:116px">Stratus Web Services
      <svg width="12" height="8" viewBox="0 0 12 8"><path d="M1 1l5 5 5-5" fill="none" stroke="#111" stroke-width="2"/></svg></div>
    <div class="abs cat-sub">Popular Courses<br>Trending Content<br>Certification Courses<br>Perfect For Beginners<br>Intermediate Courses<br>Advanced Courses</div>
    <div class="abs cat-main" style="top:331px">Nimbus Cloud
      <svg width="8" height="12" viewBox="0 0 8 12"><path d="M1 1l5 5-5 5" fill="none" stroke="#111" stroke-width="2"/></svg></div>
    <div class="abs cat-main" style="top:365px">Cirrus Compute
      <svg width="8" height="12" viewBox="0 0 8 12"><path d="M1 1l5 5-5 5" fill="none" stroke="#111" stroke-width="2"/></svg></div>
  </div>
</aside>

<h2 class="abs section-title">Popular Course</h2>

<main>
  <article class="abs card" style="left:415px;top:466px">
    <div class="thumb" role="img" aria-label="Online education illustration with laptop and study items" style="background:linear-gradient(135deg,#2b4fa8,#1aa3d9)"></div>
    <h4>How to Scale Social Impact</h4>
    <p>Lorem Ipsum is simply dummy text of the printing and typesetting .</p>
    <div class="meta"><div><svg width="11" height="11"><rect x="0.5" y="1.5" width="10" height="9" fill="none" stroke="#999"/><rect x="0.5" y="1.5" width="10" height="3" fill="#999"/></svg>22/04/2020</div><div><svg width="11" height="11"><circle cx="5.5" cy="3" r="2.6" fill="#999"/><path d="M0.5 11a5 4 0 0 1 10 0z" fill="#999"/></svg>John Doe</div></div>
    <div class="start">Start Course</div>
  </article>
  <article class="abs card" style="left:772px;top:466px">
    <div class="thumb" role="img" aria-label="Online courses illustration with a desk workstation" style="background:linear-gradient(135deg,#8b5cf6,#6b7cf0)"></div>
    <h4>How to Scale Social Impact</h4>
    <p>Lorem Ipsum is simply dummy text of the printing and typesetting .</p>
    <div class="meta"><div><svg width="11" height="11"><rect x="0.5" y="1.5" width="10" height="9" fill="none" stroke="#999"/><rect x="0.5" y="1.5" width="10" height="3" fill="#999"/></svg>22/04/2020</div><div><svg width="11" height="11"><circle cx="5.5" cy="3" r="2.6" fill="#999"/><path d="M0.5 11a5 4 0 0 1 10 0z" fill="#999"/></svg>John Doe</div></div>
    <div class="start">Start Course</div>
  </article>
  <article class="abs card" style="left:415px;top:830px">
    <div class="thumb" role="img" aria-label="E-learning illustration with a computer on a desk" style="background:linear-gradient(180deg,#14c1bb,#0fb0a8)"></div>
    <h4>How to Scale Social Impact</h4>
    <p>Lorem Ipsum is simply dummy text of the printing and typesetting .</p>
    <div class="meta"><div><svg width="11" height="11"><rect x="0.5" y="1.5" width="10" height="9" fill="none" stroke="#999"/><rect x="0.5" y="1.5" width="10" height="3" fill="#999"/></svg>22/04/2020</div><div><svg width="11" height="11"><circle cx="5.5" cy="3" r="2.6" fill="#999"/><path d="M0.5 11a5 4 0 0 1 10 0z" fill="#999"/></svg>John Doe</div></div>
    <div class="start">Start Course</div>
  </article>
  <article class="abs card" style="left:772px;top:830px">
    <div class="thumb" role="img" aria-label="Online education illustration with a phone and books" style="background:linear-gradient(135deg,#6a1b9a,#8e1b8f)"></div>
    <h4>How to Scale Social Impact</h4>
    <p>Lorem Ipsum is simply dummy text of the printing and typesetting .</p>
    <div class="meta"><div><svg width="11" height="11"><rect x="0.5" y="1.5" width="10" height="9" fill="none" stroke="#999"/><rect x="0.5" y="1.5" width="10" height="3" fill="#999"/></svg>22/04/2020</div><div><svg width="11" height="11"><circle cx="5.5" cy="3" r="2.6" fill="#999"/><path d="M0.5 11a5 4 0 0 1 10 0z" fill="#999"/></svg>John Doe</div></div>
    <div class="start">Start Course</div>
  </article>
  <article class="abs card" style="left:415px;top:1199px">
    <div class="thumb" role="img" aria-label="E-learning illustration with an open book, trophy and clock" style="background:linear-gradient(135deg,#b43ce8,#d43fe0)"></div>
    <h4>How to Scale Social Impact</h4>
    <p>Lorem Ipsum is simply dummy text of the printing and typesetting .</p>
    <div class="meta"><div><svg width="11" height="11"><rect x="0.5" y="1.5" width="10" height="9" fill="none" stroke="#999"/><rect x="0.5" y="1.5" width="10" height="3" fill="#999"/></svg>22/04/2020</div><div><svg width="11" height="11"><circle cx="5.5" cy="3" r="2.6" fill="#999"/><path d="M0.5 11a5 4 0 0 1 10 0z" fill="#999"/></svg>John Doe</div></div>
    <div class="start">Start Course</div>
  </article>
  <article class="abs card" style="left:772px;top:1199px">
    <div class="thumb" role="img" aria-label="Online course illustration with a video lesson screen and chat bubbles" style="background:linear-gradient(135deg,#6a3fe0,#4f8fe6)"></div>
    <h4>How to Scale Social Impact</h4>
    <p>Lorem Ipsum is simply dummy text of the printing and typesetting .</p>
    <div class="meta"><div><svg width="11" height="11"><rect x="0.5" y="1.5" width="10" height="9" fill="none" stroke="#999"/><rect x="0.5" y="1.5" width="10" height="3" fill="#999"/></svg>22/04/2020</div><div><svg width="11" height="11"><circle cx="5.5" cy="3" r="2.6" fill="#999"/><path d="M0.5 11a5 4 0 0 1 10 0z" fill="#999"/></svg>John Doe</div></div>
    <div class="start">Start Course</div>
  </article>
</main>

<footer>
  <h2 class="abs news-title">Want us to email you<br>occasionally with Norval news?</h2>
  <div class="abs news-form"><span class="ph">Enter your email addres</span><span class="btn">SUBSCRIBE</span></div>

  <div class="abs foot-brand">
    <div class="brand-name">NORVAL</div>
    <div class="brand-tag">LEARNING CENTRE</div>
    <p>Lorem Ipsum is simply dummy text of the printing and typesetting industry.</p>
  </div>
  <div class="abs foot-col" style="left:524px"><h5>COMPANY</h5><a>About</a><a>Courses</a><a>FAQs</a></div>
  <div class="abs foot-col" style="left:719px"><h5>GET INVOLVED</h5><a>Blog</a><a>Contact</a></div>
  <div class="abs foot-col" style="left:934px"><h5>EXTRAS</h5><a>Testimonials</a><a>FAQ</a><a>Privacy</a><a>Terms</a></div>

  <div class="abs foot-rule"></div>
  <div class="abs copyright">Copyright 2020&nbsp; Norval Learning Centre&nbsp; | All Rights Reserved</div>
  <div class="abs socials" aria-label="Social links"><span></span><span></span><span></span><span></span></div>
  <div class="abs to-top"><svg width="10" height="7" viewBox="0 0 10 7"><path d="M1 6l4-4 4 4" fill="none" stroke="#fff" stroke-width="1.6"/></svg></div>
</footer>

</body>
</html>
```